Packaging Design - Labels for Organic Body Care Range

I am re-designing the current range of our Body Care Skin Care range.

It is a range of natural and organic skin care with 5 products.

The range is currently very girly and young look but we are opting for a more of a raw, edgy, organic look so that we will be well definited as being organic.

I am attaching the Design file of the the current packaging.

I have recently used Pixel Forge to redesign our baby range and the beige background design was the one chosen:

http://www.pixelforgeo.net/project-progress.aspx?briefId=58316&show=designs So something along these lines will be preferred so that it all goes together.

Have included some design inspiration below.

Look forward to seeing your designs.
Updates

I have updated the brief and included some design inspiration for these designs.

Hope this helps

Target Market(s)

Women 25 - 50 yrs

Industry/Entity Type

Baby

Requirements
Must have
• Natural feel
organic feel
Textured look
Eco chic
Luxury feel
Boutique feel
Nice to have
• bright colours
Sutble Floral (see example designs)
Should not have
• No minimilist designs ie Marbo, Tyvan etc
No Purple, Blue, or green
Avoid too much pink

```html
<!DOCTYPE html>
<html lang="en">
<head>
<meta charset="utf-8">
<title>Wholly Radiant – Natural Organic Skin Care</title>
<link rel="stylesheet" href="https://fonts.googleapis.com/css2?family=Parisienne&family=Cinzel:wght@400;600&family=Cormorant+SC:wght@500;600&display=swap">
<style>
  :root {
    --page: #ffffff;
    --rule: #6f6f6f;
    --wood-light: #ecd8b6;
    --wood: #e4caa0;
    --wood-deep: #dcbf92;
    --mist: #e4ebec;
    --ink-grey: #66696a;
    --ink-dark: #2f2d2b;
    --label-text: #fbf6ee;
    --badge-pink: #f0d3cc;
    --badge-frame: #8f9694;
    --ornament: rgba(255, 255, 255, 0.55);
  }
  * { box-sizing: border-box; margin: 0; padding: 0; }
  html, body { width: 1200px; height: 726px; overflow: hidden; background: var(--page); }
  .board { position: relative; width: 1200px; height: 726px; background: var(--page); }
  .board-rule { position: absolute; left: 0; width: 1200px; height: 1px; background: var(--rule); }
  .board-rule--top { top: 1px; }
  .board-rule--bottom { bottom: 2px; }

  .wood {
    background:
      repeating-linear-gradient(90deg, rgba(255,255,255,0.06) 0 3px, rgba(0,0,0,0.015) 3px 9px),
      linear-gradient(180deg, var(--wood-light), var(--wood) 55%, var(--wood-deep));
  }

  .masthead { position: absolute; left: 0; top: 34px; width: 1200px; height: 175px; }
  .masthead-title {
    position: absolute; left: 40px; top: 22px;
    font-family: "Parisienne", cursive; font-size: 72px; font-weight: 400;
    color: #ffffff; line-height: 1;
  }
  .masthead-tagline {
    position: absolute; left: 51px; top: 120px;
    font-family: "Cinzel", serif; font-size: 24px; font-weight: 600;
    color: var(--ink-grey); letter-spacing: 1.5px; line-height: 1;
  }

  .label { position: absolute; left: 32px; top: 281px; width: 537px; height: 407px; overflow: hidden; }

  .label-side { position: absolute; left: 0; top: 0; width: 207px; height: 407px; }
  .label-side-cap { position: absolute; left: 0; width: 207px; background: var(--mist); }
  .label-side-cap--top { top: 0; height: 63px; }
  .label-side-cap--bottom { bottom: 0; height: 39px; }
  .cert-marks { position: absolute; left: 48px; top: 6px; display: flex; gap: 14px; }
  .cert-mark { width: 27px; height: 27px; border-radius: 50%; border: 2px solid #ffffff; }
  .label-copy {
    position: absolute; left: 14px; top: 74px; width: 180px;
    font-family: "Cormorant SC", serif; font-size: 6.6px; font-weight: 600;
    color: var(--label-text); text-align: center; line-height: 1.28;
  }
  .label-divider { position: absolute; left: 14px; top: 182px; width: 176px; border-top: 1px dashed var(--ink-dark); }
  .ingredients {
    position: absolute; left: 12px; top: 190px; width: 184px;
    font-family: "Cormorant SC", serif; font-size: 5px; font-weight: 500;
    color: var(--label-text); text-align: center; line-height: 1.35;
  }
  .ingredients-heading { display: block; font-size: 6px; margin-bottom: 3px; }
  .maker-note {
    position: absolute; left: 40px; bottom: 7px;
    font-family: "Cormorant SC", serif; font-size: 5px; font-weight: 500;
    color: var(--ink-grey); line-height: 1.3;
  }
  .recycle-mark { position: absolute; left: 134px; bottom: 10px; width: 18px; height: 18px; border: 1.5px solid #ffffff; }

  .label-front { position: absolute; left: 207px; top: 0; width: 330px; height: 407px; }
  .ornament { position: absolute; }
  .ornament--top {
    right: 0; top: 0; width: 210px; height: 190px;
    background: radial-gradient(ellipse at 65% 35%, var(--ornament), rgba(255,255,255,0.15) 55%, rgba(255,255,255,0) 72%);
  }
  .ornament--bottom {
    left: 0; bottom: 0; width: 120px; height: 200px;
    background: radial-gradient(ellipse at 30% 60%, var(--ornament), rgba(255,255,255,0.12) 55%, rgba(255,255,255,0) 72%);
  }
  .name-plate { position: absolute; left: 42px; top: 115px; width: 229px; height: 135px; }
  .name-plate svg { position: absolute; inset: 0; }
  .name-plate-title {
    position: absolute; left: 0; top: 40px; width: 229px;
    font-family: "Parisienne", cursive; font-size: 23px; color: var(--ink-dark);
    text-align: center; line-height: 0.85;
  }
  .name-plate-product {
    position: absolute; left: 0; top: 95px; width: 229px;
    font-family: "Cormorant SC", serif; font-size: 9px; font-weight: 600;
    color: var(--ink-dark); text-align: center; letter-spacing: 0.4px;
  }
  .front-claim {
    position: absolute; right: 20px; top: 338px; width: 150px;
    font-family: "Cormorant SC", serif; font-size: 7px; font-weight: 500;
    color: var(--label-text); text-align: center; line-height: 1.1;
  }
  .front-divider { position: absolute; right: 26px; top: 371px; width: 134px; border-top: 1px dashed var(--ink-dark); }
  .front-scent {
    position: absolute; right: 20px; top: 372px; width: 150px;
    font-family: "Parisienne", cursive; font-size: 14px; color: var(--ink-dark); text-align: center;
  }
  .front-volume {
    position: absolute; right: 20px; top: 391px; width: 150px;
    font-family: "Cormorant SC", serif; font-size: 7px; font-weight: 600;
    color: var(--ink-dark); text-align: center;
  }
</style>
</head>
<body>
<main class="board">
  <div class="board-rule board-rule--top"></div>

  <header class="masthead wood">
    <h1 class="masthead-title">Wholly Radiant.</h1>
    <p class="masthead-tagline">Natural Organic Skin Care</p>
  </header>

  <section class="label wood" aria-label="Healing hand and nail cream label">
    <div class="label-side">
      <div class="label-side-cap label-side-cap--top">
        <div class="cert-marks">
          <span class="cert-mark"></span><span class="cert-mark"></span><span class="cert-mark"></span>
        </div>
      </div>
      <p class="label-copy">Nourish and heal dry hands, cuticles and feet with this heavenly hand and nail cream. Absorbs quickly and protects, smoothes and softens dry skin to promote healthy hands. It contains a certified organic blend of herbs and infused with Organic Shea Butter and Organic Jojoba Seed Oil. Scented with a soothing blend of Lavender, Mandarin and Chamomile Essential Oils.</p>
      <div class="label-divider"></div>
      <p class="ingredients"><span class="ingredients-heading">Ingredients:</span>Purified water, Cocoa Butter (Theobroma Cacao), Organic Shea Butter (Butyrospermum Parkii), Vegetable Glycerin, Glyceryl Monostearate, Lecithin, Organic Locust Bean Gum, Organic Safflower Oil, Organic Avocado Oil (Persea Gratissima), Organic Jojoba Oil, Sunflower Oil, Organic Sesame Oil, Wheatgerm Oil, Evening Primrose Oil, Citric Acid, Olive Leaf Extract, Organic Aloe Vera Extract, D-Panthenol, Organic Calendula Extract, Organic Chamomile Extract, Organic Lavender Extract, Rosehip Extract, Witch Hazel Extract, Lavender Essential Oil, Mandarin Essential Oil, Chamomile Essential Oil, Rosemary Antioxidant, Vitamin E, Potassium Sorbate.</p>
      <div class="label-side-cap label-side-cap--bottom">
        <p class="maker-note">Made in Australia<br>Wholly Radiant<br>www.whollyradiant.example</p>
        <span class="recycle-mark"></span>
      </div>
    </div>

    <div class="label-front">
      <div class="ornament ornament--top" role="img" aria-label="Pale floral vine ornament"></div>
      <div class="ornament ornament--bottom" role="img" aria-label="Pale leafy sprig ornament"></div>

      <div class="name-plate">
        <svg width="229" height="135" viewBox="0 0 229 135" role="img" aria-label="Name plate with soft pink floral pattern">
          <path d="M24 6 H205 Q205 22 221 22 V113 Q205 113 205 129 H24 Q24 113 8 113 V22 Q24 22 24 6 Z"
                fill="var(--badge-pink)" stroke="var(--badge-frame)" stroke-width="2.5"/>
        </svg>
        <p class="name-plate-title">Wholly Radiant<br>Essentials</p>
        <p class="name-plate-product">Healing hand &amp; Nail cream</p>
      </div>

      <p class="front-claim">Contains an organic herbal blend, infused with organic shea butter, rosehip oil &amp; jojoba seed oil</p>
      <div class="front-divider"></div>
      <p class="front-scent">Lavender &amp; Mandarin</p>
      <p class="front-volume">100ml 3.4 fl oz</p>
    </div>
  </section>

  <div class="board-rule board-rule--bottom"></div>
</main>
</body>
</html>
```